Personal Injury Attorney Marketing Brochure to Medical Providers

We are looking to have a brochure - booklet form - outside - inside and back page - to hand out to chiropractors, physical therapist, clinics and other medical providers that treat persons who were injured - from an auto accident - truck accident - slip and fall, work related injury. We want them to know we handle personal injury work and represent persons who were injured as a result of the negligence of another person / company. We want the brochure to be professional and represent that we have a lot of experience in this area - Brian in practice since 1990 and Lena since 2000. Please refer to our website - www.fenwoodlegal.com for the type of work that we do and the practice areas. If we need to send more content - let us know. The project is to advertise only Brian Tolliver and lena Moskos.
Updates

We added a QR code to add to the brochure

Target Market(s)

Medical providers - such as chiropractors, Physical therapist, orthopedic doctors who may be able to refer a patient to a personal injury attorney who can help them pursue a personal injury claim

Industry/Entity Type

We are personal injury attorneys - we represent persons who have been injured in car accidents, trucking accidents, work site accidents, slip and falls that result in - broken bones, serious injuries and other injuries to help them get compensation

Font styles to use
Serif

Colors
0054AA
0677BA
7BADD7
CADEEF
E8F1F8

Requirements
Must have
• Photos of law firm members Brian Tolliver and Lena Moskos and our firm logo, our l numnew location address - which is 415 Wexbury Mill Rd., Norcross, GA 30071 / our direct phone numbers / e-mail address / website and information about us and our practice / Free consult / Attorney's who are very accessible / We have spanish speaking attorney and staff members. Please use only LEXRA or Google reviews for Brian Tolliver or Lena Moskos - not for Gordon Pellish. For e-mail contact to the firm - add admin@fenwoodlegal or admin3@fenwoodlegal.com - and add for Spanish - 404-555-0172 or for English - 404-555-0186
Nice to have
• Quotes from satisfied customers from Brian Tolliver and Lena Moskos's Google reviews and LEXRA reviews / our LEXRA ratings - all of which can be found on the internet - or we can provide - see attached word document with Google and LEXRA review information.
Should not have
• No guarantee of results

```html
<!DOCTYPE html>
<html lang="en">
<head>
<meta charset="utf-8">
<title>Pellish Tolliver Moskos – Brochure</title>
<link rel="stylesheet" href="https://fonts.googleapis.com/css2?family=Playfair+Display:wght@700;800&family=Montserrat:wght@400;500;600;700;800&display=swap">
<style>
:root{
  --navy:#1b2d5c;
  --navy-deep:#15244b;
  --navy-soft:#2c4377;
  --blue:#2b8fe8;
  --blue-text:#2a86dc;
  --ink:#2b2f3a;
  --muted:#5a5f6b;
  --gold:#c9a44a;
  --tan:#b89a74;
  --canvas:#e7e7e7;
  --paper:#ffffff;
  --serif:'Playfair Display', Georgia, serif;
  --sans:'Montserrat', Arial, sans-serif;
}
*{box-sizing:border-box;margin:0;padding:0}
html,body{width:1200px;height:2897px;overflow:hidden}
body{background:var(--canvas);position:relative;font-family:var(--sans);color:var(--ink)}

.page{position:absolute;background:var(--paper);overflow:hidden}

/* ---------- cover ---------- */
.cover{width:620px;height:877px}
.cover-scaled{position:absolute;left:0;top:0;transform:scale(.8387);transform-origin:0 0}
.brand{position:absolute;left:215px;top:44px}
.brand-name{font-family:var(--serif);font-weight:700;font-size:23px;color:var(--navy);letter-spacing:.5px;text-transform:uppercase}
.brand-tag{font-family:var(--sans);font-size:8px;letter-spacing:3px;color:var(--muted);margin-top:4px;text-transform:uppercase;padding-left:70px}
.cover-photo{position:absolute;left:90px;top:110px;width:455px;height:420px;
  background:linear-gradient(160deg,#3f5a33 0%,#2f4527 35%,#5d6b4e 60%,#8a8f7c 80%,#4c5a3d 100%)}
.cover-accent{position:absolute;left:545px;top:215px;width:75px;height:105px;background:var(--blue)}
.cover-band{position:absolute;left:0;top:500px;width:555px;height:215px;
  background:linear-gradient(100deg,var(--navy-deep) 0%,var(--navy) 55%,var(--navy-soft) 100%);
  padding:38px 0 0 40px;color:#fff}
.cover-title{font-family:var(--serif);font-weight:800;font-size:41px;line-height:1.12}
.cover-tagline{font-family:var(--sans);font-weight:800;font-size:15px;letter-spacing:1.5px;margin-top:10px}
.cover-url{position:absolute;left:42px;top:770px;font-size:18px;font-weight:500;color:var(--ink);letter-spacing:1px}

/* ---------- back cover ---------- */
.back{width:520px;height:735px;background:#f4f4f4}
.back-band{position:absolute;left:0;top:430px;width:520px;height:160px;background:var(--navy);padding:20px 0 0 62px;color:#fff}
.back-band::before{content:"";position:absolute;left:0;top:0;width:20px;height:48px;background:var(--blue)}
.call-line{font-size:12px;color:var(--blue);letter-spacing:1px;font-weight:500}
.contact-row{display:flex;align-items:center;gap:10px;margin-top:7px}
.contact-row svg{width:13px;height:13px;flex:none}
.contact-phone{font-size:21px;letter-spacing:2px;font-weight:500}
.contact-small{font-size:10px;letter-spacing:.8px}

/* ---------- inside pages ---------- */
.inside{width:560px;height:792px;padding:38px 42px 0}
.stat-row{display:grid;grid-template-columns:repeat(3,1fr)}
.stat-label{font-size:6.5px;font-weight:700;letter-spacing:1px;color:var(--blue-text);text-transform:uppercase;height:14px;padding-left:4px}
.stat-head{font-family:var(--serif);font-weight:700;font-size:17px;color:var(--navy);padding-left:4px}
.rule{display:block;width:30px;height:2px;background:var(--tan);margin:4px 0 6px 4px}
.stat-box{background:var(--navy);color:#fff;font-size:6.6px;line-height:1.4;padding:10px 10px;height:86px}
.stat-box.mid{background:var(--navy-deep)}
.section-head{font-family:var(--serif);font-weight:700;font-size:18px;color:var(--navy);margin-top:16px}
.section-sub{font-size:7.4px;font-weight:700;color:var(--blue-text);margin:2px 0 7px}
.body-copy p{font-size:7.2px;line-height:1.42;color:var(--ink);margin-bottom:8px;text-align:justify}
.practice{margin-top:12px;height:150px;background:linear-gradient(100deg,var(--navy-deep),var(--navy) 60%,var(--navy-soft));padding:14px 20px;color:#fff}
.practice-title{font-family:var(--serif);font-weight:700;font-size:17px}
.practice .rule{margin-left:0}
.practice-items{display:grid;grid-template-columns:repeat(3,1fr);margin-top:4px}
.practice-item{text-align:center;font-size:7.2px;font-weight:700;line-height:1.35;position:relative}
.practice-item+.practice-item::before{content:"";position:absolute;left:0;top:12px;width:1px;height:56px;background:rgba(255,255,255,.6)}
.practice-item svg{width:46px;height:46px;display:block;margin:0 auto 8px}

.review-title{font-family:var(--serif);font-weight:700;font-size:17px;color:var(--navy)}
.portrait{margin-top:10px;height:255px;background:linear-gradient(90deg,#8a7458 0%,#6d5a45 30%,#2a3350 48%,#1f2a48 56%,#7a6650 72%,#a08a6c 100%)}
.review{display:grid;grid-template-columns:80px 1fr;margin-top:16px}
.stars{color:#e2a91c;font-size:10px;letter-spacing:-1px}
.posted{font-size:5.6px;font-style:italic;color:var(--muted);line-height:1.3;margin-top:2px}
.review-head{font-size:8px;font-weight:700;color:var(--blue-text);margin-bottom:5px}
.review-text{font-size:7.2px;line-height:1.4;color:var(--ink)}
.review-text em{font-weight:700}

.page-foot{position:absolute;left:42px;right:58px;bottom:30px;height:16px;display:flex;align-items:center}
.foot-brand{font-family:var(--serif);font-weight:700;font-size:8px;color:var(--navy);text-transform:uppercase;white-space:nowrap}
.foot-line{flex:1;height:1px;background:var(--navy);margin:0 0 0 10px;align-self:flex-end}
.foot-url{background:var(--navy);color:#fff;font-size:8px;padding:3px 8px 3px 22px;clip-path:polygon(12px 0,100% 0,100% 100%,0 100%)}
.foot-num{position:absolute;right:-16px;top:0;width:16px;height:16px;background:var(--blue);color:#fff;font-size:7px;display:flex;align-items:center;justify-content:center}
</style>
</head>
<body>

<!-- front cover -->
<section class="page cover" style="left:290px;top:90px">
  <div class="brand">
    <div class="brand-name">Pellish Tolliver Moskos</div>
    <div class="brand-tag">Attorneys at Law</div>
  </div>
  <div class="cover-photo" role="img" aria-label="Photo of the firm's three attorneys standing together outdoors among trees"></div>
  <div class="cover-accent"></div>
  <div class="cover-band">
    <h1 class="cover-title">Dedicated Georgia<br>Injury Lawyers</h1>
    <p class="cover-tagline">-DRIVEN. ATTENTIVE. RELIABLE.</p>
  </div>
  <p class="cover-url">www.fenwoodlegal.com</p>
</section>

<!-- back cover + front cover spread -->
<section class="page back" style="left:80px;top:1107px">
  <div class="back-band">
    <p class="call-line">call us today se habla español</p>
    <div class="contact-row">
      <svg viewBox="0 0 24 24" fill="#fff"><path d="M6.6 10.8a15 15 0 0 0 6.6 6.6l2.2-2.2a1 1 0 0 1 1-.25 11.4 11.4 0 0 0 3.6.57 1 1 0 0 1 1 1V20a1 1 0 0 1-1 1A17 17 0 0 1 3 4a1 1 0 0 1 1-1h3.5a1 1 0 0 1 1 1c0 1.25.2 2.45.57 3.57a1 1 0 0 1-.25 1z"/></svg>
      <span class="contact-phone">(404) 555-0143</span>
    </div>
    <div class="contact-row">
      <svg viewBox="0 0 24 24" fill="#fff"><path d="M12 2a7 7 0 0 0-7 7c0 5.25 7 13 7 13s7-7.75 7-13a7 7 0 0 0-7-7zm0 9.5A2.5 2.5 0 1 1 12 6.5a2.5 2.5 0 0 1 0 5z"/></svg>
      <span class="contact-small">415 Wexbury Mill Rd., Norcross, GA 30071</span>
    </div>
    <div class="contact-row">
      <svg viewBox="0 0 24 24" fill="#fff"><path d="M3 5h18v14H3z M3 5l9 7 9-7" stroke="#1b2d5c" stroke-width="1.5"/></svg>
      <span class="contact-small">info@fenwoodlegal.com</span>
    </div>
    <div class="contact-row">
      <svg viewBox="0 0 24 24" fill="none" stroke="#fff" stroke-width="2"><circle cx="12" cy="12" r="9"/><path d="M3 12h18M12 3c3 3 3 15 0 18M12 3c-3 3-3 15 0 18"/></svg>
      <span class="contact-small">www.fenwoodlegal.com</span>
    </div>
  </div>
</section>
<section class="page" style="left:600px;top:1107px;width:520px;height:735px">
  <div class="cover cover-scaled page" style="position:absolute">
    <div class="brand">
      <div class="brand-name">Pellish Tolliver Moskos</div>
      <div class="brand-tag">Attorneys at Law</div>
    </div>
    <div class="cover-photo" role="img" aria-label="Photo of the firm's three attorneys standing together outdoors among trees"></div>
    <div class="cover-accent"></div>
    <div class="cover-band">
      <h2 class="cover-title">Dedicated Georgia<br>Injury Lawyers</h2>
      <p class="cover-tagline">-DRIVEN. ATTENTIVE. RELIABLE.</p>
    </div>
    <p class="cover-url">www.fenwoodlegal.com</p>
  </div>
</section>

<!-- inside spread: firm page -->
<section class="page inside" style="left:40px;top:1982px">
  <div class="stat-row">
    <div><p class="stat-label">80+ Years of Experience</p><h3 class="stat-head">On Your Side</h3><span class="rule"></span></div>
    <div><p class="stat-label">Recovered</p><h3 class="stat-head">Millions</h3><span class="rule"></span></div>
    <div><p class="stat-label">Our Attorneys Are</p><h3 class="stat-head">Attentive</h3><span class="rule"></span></div>
    <p class="stat-box">We know how the insurance industry functions and how to maximize results for our injured clients. Should your case be tried by a jury, we are more than confident in the courtroom.</p>
    <p class="stat-box mid">Since opening our firm we have had a very high level of success in our plaintiff's cases.</p>
    <p class="stat-box">When you retain our Georgia injury attorneys, you never work with a "case manager". We know our clients and we respond to their questions and concerns and keep them informed and involved every step of the way.</p>
  </div>

  <h3 class="section-head">Our Firm</h3>
  <span class="rule" style="margin-left:0"></span>
  <p class="section-sub">Dedicated to Accomplishing the Results You Want</p>
  <div class="body-copy">
    <p>At Pellish Tolliver Moskos, LLC we are passionate about helping our injury clients achieve excellent results and recover the money they deserve. We have in-depth experience as trial attorneys defending insurance companies and their insureds. Because we have in the past dealt directly with claims representatives and insurance adjusters as our clients, we have unique insight into how insurance companies work and what they need to resolve cases at the maximum level possible.</p>
    <p>We use this knowledge and put it to work for you, our client. Whether you were injured in a car accident, slip and fall, construction site accident, trucking accident, nursing home abuse or any other injury that was the fault of someone else, we are committed to obtaining the best result possible. If you have suffered an injury as the result of the negligence or fault of another person or company, rest assured that our attorneys will provide the knowledge and support you need to help you overcome this difficult time.</p>
    <p>Our attorneys work diligently to secure the facts and the evidence needed to maximize your compensation. If your case should proceed to trial, PTM is ready with decades of courtroom experience to fully present your case to the jury and achieve the best result possible in that setting. Should you decide to hire our lawyers, you will feel a peace of mind in knowing you have retained the services of an experienced, respected and reputable Georgia law firm. We build lasting relationships with our clients. Dependable. Attentive. Reliable. PTM.</p>
  </div>

  <div class="practice">
    <h3 class="practice-title">Our practice</h3>
    <span class="rule"></span>
    <div class="practice-items">
      <div class="practice-item">
        <svg viewBox="0 0 48 48"><circle cx="24" cy="24" r="22" fill="#fff"/><circle cx="24" cy="24" r="18" fill="none" stroke="#2b8fe8" stroke-width="2"/><circle cx="24" cy="24" r="10" fill="none" stroke="#1b2d5c" stroke-width="2"/><circle cx="24" cy="24" r="4" fill="#1b2d5c"/><path d="M24 24l10-10" stroke="#1b2d5c" stroke-width="2"/></svg>
        Free consult
      </div>
      <div class="practice-item">
        <svg viewBox="0 0 48 48"><circle cx="24" cy="24" r="22" fill="#fff"/><circle cx="24" cy="24" r="18" fill="none" stroke="#2b8fe8" stroke-width="2"/><rect x="22" y="13" width="11" height="22" fill="none" stroke="#1b2d5c" stroke-width="2"/><path d="M13 24h11M20 20l4 4-4 4" fill="none" stroke="#1b2d5c" stroke-width="2"/></svg>
        Attorney's who<br>are very accessible
      </div>
      <div class="practice-item">
        <svg viewBox="0 0 48 48"><circle cx="24" cy="24" r="22" fill="#fff"/><circle cx="24" cy="24" r="18" fill="none" stroke="#2b8fe8" stroke-width="2"/><circle cx="20" cy="19" r="4" fill="#1b2d5c"/><circle cx="29" cy="20" r="3.5" fill="#1b2d5c"/><path d="M12 33c0-5 4-8 8-8s8 3 8 8zM26 33c0-4 1-6 3-7 4 0 7 3 7 7z" fill="#1b2d5c"/></svg>
        We have spanish<br>speaking attorney and<br>staff members.
      </div>
    </div>
  </div>

  <div class="page-foot">
    <span class="foot-brand">Pellish Tolliver Moskos</span>
    <span class="foot-line"></span>
    <span class="foot-url">www.fenwoodlegal.com</span>
    <span class="foot-num">01</span>
  </div>
</section>

<!-- inside spread: reviews page -->
<section class="page inside" style="left:600px;top:1982px">
  <h3 class="review-title">LEXRA Reviews for Brian Tolliver</h3>
  <div class="portrait" role="img" aria-label="Portrait of attorney Brian Tolliver in a navy suit leaning against a stone wall"></div>

  <article class="review">
    <div><p class="stars">★★★★★</p><p class="posted">Posted by Dana R.<br>July 23, 2021</p></div>
    <div>
      <h4 class="review-head">Excellent Injury Accident Attorney and Negotiator</h4>
      <p class="review-text">I interviewed several attorneys before settling on Brian Tolliver for legal representation. My comfort level with him was immediate and I knew I could count on him to handle my auto accident claim and get me a reasonable settlement. He handled everything including all negotiations with the at-fault party's insurance company and coordinating repaying my health insurance company, which was an ERISA plan.</p>
    </div>
  </article>

  <article class="review">
    <div><p class="stars">★★★★★</p><p class="posted">Posted by Dana R.<br>July 23, 2021</p></div>
    <div>
      <h4 class="review-head">Exemplary and Empathetic—beyond satisfied</h4>
      <p class="review-text">Brian was the most understanding, attentive and caring lawyer I could ever ask for. After being injured in an accident, I was unable to continue working. Consequently, the bills were piling up and I had no resources to turn to. Brian handled my case with such compassion and diligence and made sure to provide me with the utmost attention throughout such a worrisome time. His communication was consistently prompt which put me at ease during such a sensitive process. I will be recommending Brian and his firm to all of my friends and family.<br><em>-- Sincerely, Marisa.</em></p>
    </div>
  </article>

  <article class="review">
    <div><p class="stars">★★★★★</p><p class="posted">Posted by Dana R.<br>July 23, 2021</p></div>
    <div>
      <h4 class="review-head">Mr</h4>
      <p class="review-text">I was in a auto accident 9-26-06 and was life flighted to Brookmere Hospital in Atlanta. I was in a coma for several weeks and when I came out of it my wife had met and hired Mr Brian Tolliver to help us with the legalities we had in front of us. I am a very simple minded person and Brian was right there for us every step of the way he is very easy to talk to and we were always comfortable dealing with him.</p>
    </div>
  </article>

  <div class="page-foot">
    <span class="foot-brand">Pellish Tolliver Moskos</span>
    <span class="foot-line"></span>
    <span class="foot-url">www.fenwoodlegal.com</span>
    <span class="foot-num">01</span>
  </div>
</section>

</body>
</html>
```